Criação de Logo + Papelaria + Manual Básico para Alimentos & Bebidas
" Empresa pequena, ambiental e socialmente responsável, sediada na caatinga baiana, à beira do Rio São Francisco, abastecida por matérias primas de produtores locais. "

```html
<!DOCTYPE html>
<html lang="pt-BR">
<head>
<meta charset="UTF-8">
<title>Cartão de visita – Vereda</title>
<link href="https://fonts.googleapis.com/css2?family=Open+Sans:wght@400;600;700&display=swap" rel="stylesheet">
<style>
  :root {
    --page-bg: #eeeeec;
    --card-bg: #2b2b2b;
    --card-text: #ffffff;
    --card-muted: #d9d9d9;
    --rule: #9a9a9a;
    --brand-green: #4f8a3c;
  }
  html, body {
    margin: 0;
    width: 1200px;
    height: 1200px;
    overflow: hidden;
    background: var(--page-bg);
  }
  .business-card {
    position: absolute;
    left: 100px;
    top: 452px;
    width: 1000px;
    height: 296px;
    font-family: "Open Sans", Arial, sans-serif;
  }
  .card-shape { fill: var(--card-bg); }
  .person-name { fill: var(--card-text); font-size: 31px; font-weight: 600; }
  .person-role { fill: var(--card-text); font-size: 19px; font-weight: 700; }
  .contact-line { fill: var(--card-muted); font-size: 20px; font-weight: 400; }
  .contact-web { fill: var(--card-text); font-size: 20px; font-weight: 700; }
  .name-rule, .divider { stroke: var(--rule); stroke-width: 2; }
  .icon { fill: none; stroke: var(--card-muted); stroke-width: 2.2; stroke-linecap: round; stroke-linejoin: round; }
  .social-dot { fill: var(--card-muted); }
  .brand-mark { fill: var(--brand-green); }
  .brand-name { fill: var(--card-text); font-size: 56px; font-weight: 700; }
</style>
</head>
<body>
  <svg class="business-card" viewBox="0 0 1000 296" xmlns="http://www.w3.org/2000/svg">
    <path class="card-shape" d="M0,0 H900 Q1000,0 1000,100 V296 H44 Q0,296 0,252 Z"/>

    <g class="contact-side">
      <text class="person-name" x="121" y="52">Nome Sobrenome</text>
      <line class="name-rule" x1="121" y1="66" x2="405" y2="66"/>
      <text class="person-role" x="121" y="92">Cargo Nome</text>

      <g class="icon phone-icon" transform="translate(128,137) scale(0.75)">
        <path d="M2,2 L8,2 L10,8 L7,10 Q10,16 15,18 L17,15 L23,17 L23,23 Q10,24 2,8 Z"/>
      </g>
      <text class="contact-line" x="177" y="140">+ 55 00 90000 0000</text>
      <text class="contact-line" x="177" y="162">+ 55 00 0000 0000</text>

      <g class="icon globe-icon" transform="translate(138,224)">
        <circle r="9"/>
        <ellipse rx="4" ry="9"/>
        <line x1="-9" y1="0" x2="9" y2="0"/>
      </g>
      <text class="contact-line" x="177" y="212">contato@site.com.br</text>
      <text class="contact-web" x="177" y="236">www.site.com.br</text>
      <circle class="social-dot" cx="379" cy="229" r="9"/>
      <circle class="social-dot" cx="401" cy="229" r="9"/>
    </g>

    <line class="divider" x1="527" y1="28" x2="527" y2="252"/>

    <g class="brand-side">
      <circle class="brand-mark" cx="730" cy="92" r="34"/>
      <text class="brand-name" x="730" y="200" text-anchor="middle">VEREDA</text>
    </g>
  </svg>
</body>
</html>
```